Flaschenetikett Jörgi`s ColaMix
Zielgruppe
Wir machen einen ColaMix, weil wir es können und ihm eine Prise 80er verpassen wollen.
Hip, Trendig und ein bisschen Oldschool.
Bei uns kommt nur in die Flasche, was uns selber schmeckt und dabei preislich fair ist! Kein Schnickschnack, dafür mit viel Geschmack und einer Portion Oldschool.
Einfach einen richtig guten Brauso ähhmm, ColaMix!
Farben:
orange / weiss (Hintergrund Orange & Schrift Weiss)
oder
weiss / anthrazit
Flaschenfarbe:
braun
Etikettgröße:
max. 10 x 10 cm
Name:
Jörgis ColaMix
Zusatztext:
MÜNCHEN
ColaMix (muss irgendwo auf dem Etikett stehen)
Die Beispiele finden wir ultra hip, ein bisschen oldschool, trendig und genau richtig. Alles simpel, kein BlimBlim aber dafür einen ziemlich hohen Stylfaktor.
Wir sind nicht modern, sondern Kinder der 80iger, stehen auf Industrie Vintage Zeug und brauchen einen "ColaMix" der zu uns passt.
Jörg, ja einfach Jörg soll er heissen. Ein deutscher Trendname aus dem 19.Jahrhundert und doch jung und frisch! Genau wie unser ColaMix.
Das Kultgetränk das Allen schmeckt kommt in einer Oldschool braunen Flasche um die Ecke.
WIR MACHEN UNS FAST IN DIE HOSEN VOR AUFREGUNG, WAS IHR SO AUF DER FLASCHE HABT!!!!
HAUT REIN!!!

```html
<!DOCTYPE html>
<html lang="de">
<head>
<meta charset="utf-8">
<title>Jörgis ColaMix – Flaschenetikett</title>
<link rel="stylesheet" href="https://fonts.googleapis.com/css2?family=Josefin+Sans:wght@600;700&display=swap">
<style>
  :root {
    --orange: #f26d1d;
    --orange-stripe: #f5803a;
    --white: #ffffff;
  }
  html, body {
    margin: 0;
    padding: 0;
    width: 1200px;
    height: 1200px;
    overflow: hidden;
    background: var(--orange);
  }
  .canvas {
    position: relative;
    width: 1200px;
    height: 1200px;
    background: var(--orange);
  }
  .label {
    position: absolute;
    left: 150px;
    top: 150px;
    width: 900px;
    height: 900px;
    display: block;
  }
  .frame { fill: none; stroke: var(--white); }
  .stripe { stroke: var(--orange-stripe); stroke-width: 5; }
  .band { fill: var(--white); }
  .band-rule { stroke: var(--orange); stroke-width: 3; }
  .brand-name {
    font-family: "Josefin Sans", sans-serif;
    font-weight: 700;
    font-size: 170px;
    fill: var(--white);
  }
  .since {
    font-family: "Josefin Sans", sans-serif;
    font-weight: 600;
    font-size: 24px;
    letter-spacing: 6px;
    fill: var(--white);
  }
  .product-name {
    font-family: "Josefin Sans", sans-serif;
    font-weight: 700;
    font-size: 110px;
    fill: var(--orange);
  }
  .tagline {
    font-family: "Josefin Sans", sans-serif;
    font-weight: 600;
    font-size: 32px;
    letter-spacing: 5px;
    fill: var(--white);
  }
</style>
</head>
<body>
<main class="canvas">
  <svg class="label" viewBox="0 0 816 816" xmlns="http://www.w3.org/2000/svg" aria-label="Flaschenetikett Jörgis ColaMix">
    <rect class="frame" x="7" y="7" width="802" height="802" stroke-width="14"/>

    <g class="stripes">
      <line class="stripe" x1="40" x2="776" y1="48" y2="48"/>
      <line class="stripe" x1="40" x2="776" y1="72" y2="72"/>
      <line class="stripe" x1="40" x2="776" y1="96" y2="96"/>
      <line class="stripe" x1="40" x2="776" y1="120" y2="120"/>
      <line class="stripe" x1="40" x2="776" y1="144" y2="144"/>
      <line class="stripe" x1="40" x2="776" y1="168" y2="168"/>
      <line class="stripe" x1="40" x2="776" y1="192" y2="192"/>
      <line class="stripe" x1="40" x2="776" y1="216" y2="216"/>
      <line class="stripe" x1="40" x2="776" y1="240" y2="240"/>
      <line class="stripe" x1="40" x2="776" y1="264" y2="264"/>
      <line class="stripe" x1="40" x2="776" y1="288" y2="288"/>
      <line class="stripe" x1="40" x2="776" y1="312" y2="312"/>
      <line class="stripe" x1="40" x2="776" y1="336" y2="336"/>
      <line class="stripe" x1="40" x2="776" y1="360" y2="360"/>
      <line class="stripe" x1="40" x2="776" y1="384" y2="384"/>
      <line class="stripe" x1="40" x2="776" y1="408" y2="408"/>
      <line class="stripe" x1="40" x2="776" y1="432" y2="432"/>
      <line class="stripe" x1="40" x2="776" y1="456" y2="456"/>
    </g>
    <path class="frame" d="M16 486 V16 H800 V486" stroke-width="4"/>
    <path class="frame" d="M28 486 V28 H788 V486" stroke-width="3"/>

    <text class="brand-name" x="408" y="320" text-anchor="middle" textLength="600" lengthAdjust="spacingAndGlyphs">JÖRGI</text>

    <path id="since-arc" d="M290 378 Q 408 432 526 378" fill="none"/>
    <text class="since"><textPath href="#since-arc" startOffset="50%" text-anchor="middle">SINCE 2016</textPath></text>

    <rect class="band" x="12" y="492" width="792" height="176"/>
    <line class="band-rule" x1="12" x2="804" y1="496" y2="496"/>
    <line class="band-rule" x1="12" x2="804" y1="656" y2="656"/>
    <text class="product-name" x="408" y="614" text-anchor="middle">ColaMix</text>

    <rect class="frame" x="16" y="686" width="784" height="114" stroke-width="4"/>
    <rect class="frame" x="28" y="698" width="760" height="90" stroke-width="3"/>
    <text class="tagline" x="408" y="755" text-anchor="middle">MADE FOR MUNICH</text>
  </svg>
</main>
</body>
</html>
```